Strength Coach Business Card Design Project

I would like a business card design to complement my new logo. I would like the card to be clean, seek and strong!

Target Market(s)

Mostly adults and junior atheletes who are serious about changing their lives.

Industry/Entity Type

Business

Font styles to use
Serif

Colors

Designer to choose colors to be used in the design.

```html
<!DOCTYPE html>
<html lang="en">
<head>
<meta charset="utf-8">
<title>Ridge Strength and Fitness – Business Card</title>
<link href="https://fonts.googleapis.com/css2?family=Source+Sans+3:wght@400;600;700&display=swap" rel="stylesheet">
<style>
  :root {
    --backdrop: #e9e6e2;
    --card-white: #ececec;
    --panel-dark: #2b2b2c;
    --accent-red: #d32f2f;
    --ink: #2e2e2e;
    --text-light: #f2f2f2;
    --mark-grey: #8a8a8a;
  }
  * { margin: 0; padding: 0; box-sizing: border-box; }
  html, body { width: 1200px; height: 720px; overflow: hidden; }
  body {
    background: var(--backdrop);
    font-family: "Source Sans 3", "Helvetica Neue", Arial, sans-serif;
    display: flex; align-items: center; justify-content: center;
  }
  .card {
    position: relative;
    width: 1050px; height: 600px;
    background: var(--card-white);
    box-shadow: 0 10px 30px rgba(0,0,0,0.18);
    overflow: hidden;
  }
  .card-shapes { position: absolute; inset: 0; }
  .brand-name {
    position: absolute; left: 64px; top: 220px;
    color: var(--ink); font-weight: 700; line-height: 1;
  }
  .brand-name .primary { display: block; font-size: 136px; letter-spacing: 4px; }
  .brand-name .secondary { display: block; font-size: 34px; letter-spacing: 3px; margin-top: 12px; }
  .identity {
    position: absolute; right: 60px; top: 44px; text-align: right;
  }
  .identity .person-name { color: var(--accent-red); font-size: 40px; font-weight: 400; }
  .identity .person-title { color: var(--text-light); font-size: 24px; margin-top: -4px; }
  .brand-square {
    position: absolute; right: 150px; top: 160px;
    width: 120px; height: 120px; background: var(--mark-grey);
  }
  .contact-list {
    position: absolute; right: 60px; top: 340px;
    list-style: none; text-align: right;
    color: var(--text-light); font-size: 21px; line-height: 1.6;
  }
  .contact-list li { display: flex; justify-content: flex-end; align-items: center; gap: 14px; }
  .contact-list svg { width: 20px; height: 20px; flex: none; }
  .contact-list .address-line2 { padding-right: 34px; }
</style>
</head>
<body>
  <div class="card">
    <svg class="card-shapes" viewBox="0 0 1050 600" preserveAspectRatio="none" aria-hidden="true">
      <path d="M520 0 C700 80 720 300 700 600 L1050 600 L1050 0 Z" fill="var(--panel-dark)"/>
      <path d="M450 0 C680 80 700 300 682 600 L700 600 C720 300 700 80 520 0 Z" fill="var(--accent-red)"/>
    </svg>

    <div class="brand-name">
      <span class="primary">RIDGE</span>
      <span class="secondary">STRENGTH AND FITNESS</span>
    </div>

    <div class="identity">
      <div class="person-name">Dan Mercer</div>
      <div class="person-title">Manager</div>
    </div>

    <div class="brand-square"></div>

    <ul class="contact-list">
      <li>danmercer@example.com
        <svg viewBox="0 0 20 20"><rect x="1.5" y="4" width="17" height="12" fill="none" stroke="var(--accent-red)" stroke-width="1.6"/><path d="M1.5 4 L10 11 L18.5 4" fill="none" stroke="var(--accent-red)" stroke-width="1.6"/></svg>
      </li>
      <li>912 - 555- 0148
        <svg viewBox="0 0 20 20"><rect x="5.5" y="1.5" width="9" height="17" rx="1.5" fill="none" stroke="var(--accent-red)" stroke-width="1.6"/><rect x="7.5" y="4" width="5" height="8" fill="var(--accent-red)"/></svg>
      </li>
      <li>912 - 555- 0193
        <svg viewBox="0 0 20 20"><path d="M2 8 Q10 1 18 8 L15 10 L13 7 L7 7 L5 10 Z" fill="var(--accent-red)"/><rect x="4" y="10" width="12" height="7" rx="1" fill="var(--accent-red)"/></svg>
      </li>
      <li>214 Oak Ridge Avenue,
        <svg viewBox="0 0 20 20"><path d="M10 19 C4 12 4 9 4 8 A6 6 0 0 1 16 8 C16 9 16 12 10 19 Z" fill="var(--accent-red)"/><circle cx="10" cy="8" r="2.2" fill="var(--panel-dark)"/></svg>
      </li>
      <li class="address-line2">Brookvale, NY 10482</li>
    </ul>
  </div>
</body>
</html>
```